BrawnCrate placard

I need a placard designed that will go in my monthly subscription boxes to describe the products inside. There must be space to write 3-5 sentences on each product.
the first area will be titled: For your flowing mane
2 for your macho glow
3 to keep you smelling macho
4 to keep you clanging and banging at the gym.
Placard will be 5inchs wide and 7inchs long

I have attached the logo and the website address must be used in the design brawncrates.com.

Target Market(s)

men between 20-50

Colors

Designer to choose colors to be used in the design.

Requirements
Must have
• My website address brawncrates.com
• 4 area to write 3-5 sentences
• 1 for your flowing mane
• 2to keep you smelling macho
• 3 to keep you clanging and banging at the gym
• 4 for your macho glow

```html
<!DOCTYPE html>
<html lang="en">
<head>
<meta charset="utf-8">
<title>BrawnCrate Placard</title>
<link rel="stylesheet" href="https://fonts.googleapis.com/css2?family=Roboto+Condensed:wght@400;700&family=Montserrat:wght@700&display=swap">
<style>
  :root {
    --page-bg: #e4e4e4;
    --card-bg: #191919;
    --gold: #c9a04a;
    --pennant: #dcdcdc;
    --ink-dark: #1e1e1e;
    --text-light: #ececec;
    --photo-dark: #1c1c1c;
    --photo-mid: #3a3633;
  }
  * { margin: 0; padding: 0; box-sizing: border-box; }
  html, body {
    width: 1200px; height: 856px; overflow: hidden;
    background: var(--page-bg);
  }
  .placard-frame {
    position: absolute;
    left: 314px; top: 28px;
    width: 482px; height: 675px;
    transform: scale(1.185);
    transform-origin: top left;
  }
  .placard {
    position: relative;
    width: 482px; height: 675px;
    background: var(--card-bg);
    overflow: hidden;
    font-family: "Roboto Condensed", "Arial Narrow", sans-serif;
  }
  .hero-photo {
    position: absolute;
    left: 200px; top: 82px; width: 282px; height: 540px;
    background:
      radial-gradient(ellipse at 70% 35%, var(--photo-mid) 0%, rgba(40,37,35,0.6) 40%, rgba(25,25,25,0) 75%),
      linear-gradient(90deg, var(--card-bg) 0%, var(--photo-dark) 40%, #2a2725 100%);
  }
  .top-band {
    position: absolute; left: 0; top: 28px; width: 482px; height: 54px;
    background: var(--gold);
  }
  .pennant {
    position: absolute; left: 24px; top: 0; width: 267px; height: 243px;
  }
  .brand-name {
    position: absolute; left: 24px; top: 150px; width: 267px;
    display: flex; align-items: center; justify-content: center; gap: 8px;
    font-family: "Montserrat", sans-serif; font-weight: 700;
    font-size: 25px; color: var(--ink-dark); letter-spacing: 0.5px;
  }
  .brand-mark {
    width: 18px; height: 18px; background: var(--gold);
  }
  .product-list {
    position: absolute; left: 24px; top: 266px; width: 450px;
  }
  .product {
    display: flex; gap: 9px; height: 89.5px;
  }
  .product-photo {
    flex: none; width: 88px; height: 80px;
    background: linear-gradient(135deg, #3d3f4a 0%, #22232a 100%);
  }
  .product-photo.scent { background: linear-gradient(135deg, #4a5560 0%, #8a2a2a 100%); }
  .product-photo.gym { background: linear-gradient(135deg, #d8d8d8 0%, #2a2f3a 100%); }
  .product-photo.glow { background: linear-gradient(135deg, #5a4a4a 0%, #3a3030 100%); }
  .product-title {
    font-weight: 700; font-size: 16px; line-height: 18px;
    color: var(--gold); text-transform: uppercase; white-space: nowrap;
  }
  .product-text {
    margin-top: 3px; padding-left: 2px;
    font-size: 14px; line-height: 17.5px; color: var(--text-light);
  }
  .footer-band {
    position: absolute; left: 0; top: 622px; width: 482px; height: 53px;
    background: var(--gold);
    display: flex; align-items: center; justify-content: center;
  }
  .site-url {
    font-family: "Montserrat", sans-serif; font-weight: 700;
    font-size: 15px; letter-spacing: 13px; color: var(--ink-dark);
    text-transform: uppercase; margin-right: -13px;
  }
</style>
</head>
<body>
<div class="placard-frame">
  <main class="placard">
    <div class="hero-photo" role="img" aria-label="Moody portrait of a bearded man fading into the dark background"></div>
    <div class="top-band"></div>
    <svg class="pennant" viewBox="0 0 267 243" aria-hidden="true">
      <polygon points="0,0 267,0 267,188 134,243 0,188" fill="var(--pennant)"/>
    </svg>
    <div class="brand-name"><span class="brand-mark"></span>BrawnCrate</div>

    <section class="product-list">
      <article class="product">
        <div class="product-photo mane" role="img" aria-label="Photo of a beard care product tin"></div>
        <div>
          <h2 class="product-title">For your flowing mane</h2>
          <p class="product-text">I need a placard designed that will go in my monthly sub-<br>scription boxes to describe the products inside. There<br>must be space to write 3-5 sentences on each product.</p>
        </div>
      </article>
      <article class="product">
        <div class="product-photo scent" role="img" aria-label="Photo of a grooming pomade tin"></div>
        <div>
          <h2 class="product-title">To keep you &nbsp;smelling macho</h2>
          <p class="product-text">I need a placard designed that will go in my monthly sub-<br>scription boxes to describe the products inside. There<br>must be space to write 3-5 sentences on each product.</p>
        </div>
      </article>
      <article class="product">
        <div class="product-photo gym" role="img" aria-label="Photo of sports nutrition and body products"></div>
        <div>
          <h2 class="product-title">To keep you &nbsp;clanging &amp; banging at the gym.</h2>
          <p class="product-text">I need a placard designed that will go in my monthly sub-<br>scription boxes to describe the products inside. There<br>must be space to write 3-5 sentences on each product.</p>
        </div>
      </article>
      <article class="product">
        <div class="product-photo glow" role="img" aria-label="Photo of a branded skin care pouch"></div>
        <div>
          <h2 class="product-title">For your macho glow</h2>
          <p class="product-text">I need a placard designed that will go in my monthly sub-<br>scription boxes to describe the products inside. There<br>must be space to write 3-5 sentences on each product.</p>
        </div>
      </article>
    </section>

    <footer class="footer-band">
      <span class="site-url">brawncrates.com</span>
    </footer>
  </main>
</div>
</body>
</html>
```